Medical Device Packaging Project 4 of 5

We are a medical device startup company needing packaging for a total of 5 device brands. This is posting 4 of 5 and the device name is "Velonra"

Velonra is an intraocular lens for use in cataract surgery. The target market is Chinese ophthalmologists. The box should be sophisticated and upmarket.

The company name is Brenvik Optics, I have included the logo in the uploaded files section. You should include the logo on the box.

I have uploaded a sample lens boxes from other companies that demonstrate the information needed to be contained on the box in terms of address, warnings, symbols, etc.

I have also uploaded the blank dieline of the boxes

You are welcome and encouraged to also submit to projects 1, 2, 3, and 5 as well. The same rules and expectations apply.

Industry/Entity Type

It Company

Requirements
Should not have
• Should not have any images of an eye or any bionic/futuristic feel to the design
• Note that the calvisens box is for text reference only. You may use the lens image but the futuristic/bionic look is NOT what we are going for with this brand. It should be traditional upmarket medical device artwork.

```html
<!DOCTYPE html>
<html lang="en">
<head>
<meta charset="utf-8">
<title>Velonra – Brenvik Optics Box Front</title>
<link rel="stylesheet" href="https://fonts.googleapis.com/css2?family=Michroma&family=Montserrat:wght@500;600&display=swap">
<style>
  :root {
    --stage-top: #ffffff;
    --stage-bottom: #e4e4e4;
    --panel-light: #fbfaef;
    --panel-tint: #eeeabf;
    --brand-navy: #1f3f7a;
    --brand-ring: #8fc0dc;
    --product-gold: #a3962c;
    --lens-light: #ececec;
    --lens-mid: #b4b4b4;
  }
  * { box-sizing: border-box; margin: 0; padding: 0; }
  html, body {
    width: 1200px;
    height: 782px;
    overflow: hidden;
  }
  body {
    background: radial-gradient(ellipse at 50% 40%, var(--stage-top) 0%, var(--stage-bottom) 100%);
    font-family: "Montserrat", sans-serif;
    display: flex;
    align-items: center;
    justify-content: center;
  }
  .box-front {
    position: relative;
    width: 720px;
    height: 590px;
    background: linear-gradient(135deg, var(--panel-light) 0%, var(--panel-tint) 100%);
    box-shadow: 0 18px 40px rgba(0,0,0,0.12);
    overflow: hidden;
  }
  .panel-texture {
    position: absolute;
    inset: 0;
    background: linear-gradient(160deg, rgba(255,255,255,0.55) 0%, rgba(255,255,255,0) 55%, rgba(214,205,140,0.25) 100%);
  }
  .brand-mark {
    position: absolute;
    left: 48px;
    top: 108px;
    display: flex;
    align-items: center;
    gap: 12px;
  }
  .brand-dot {
    width: 20px;
    height: 20px;
    border-radius: 50%;
    background: var(--brand-ring);
  }
  .brand-name {
    font-weight: 600;
    font-size: 20px;
    letter-spacing: 3px;
    color: var(--brand-navy);
    text-transform: uppercase;
    white-space: nowrap;
  }
  .device-type {
    position: absolute;
    right: 36px;
    top: 78px;
    font-weight: 500;
    font-size: 13px;
    letter-spacing: 0.5px;
    color: var(--brand-navy);
    text-transform: uppercase;
    white-space: nowrap;
  }
  .lens-illustration {
    position: absolute;
    left: 215px;
    top: 150px;
    width: 290px;
    height: 270px;
    border-radius: 50%;
    background: radial-gradient(ellipse closest-side at 50% 50%, var(--lens-light) 0%, var(--lens-mid) 55%, rgba(180,180,180,0) 100%);
  }
  .product-block {
    position: absolute;
    left: 48px;
    bottom: 44px;
  }
  .product-name {
    font-family: "Michroma", sans-serif;
    font-weight: 400;
    font-size: 30px;
    letter-spacing: 4px;
    color: var(--product-gold);
    text-transform: uppercase;
    line-height: 1.1;
  }
  .product-feature {
    font-weight: 500;
    font-size: 16px;
    letter-spacing: 0.5px;
    color: var(--product-gold);
    text-transform: uppercase;
    margin-top: 4px;
  }
</style>
</head>
<body>
  <main class="box-front">
    <div class="panel-texture" role="img" aria-label="Soft faceted triangle pattern in pale yellow tones"></div>

    <div class="brand-mark">
      <span class="brand-dot"></span>
      <span class="brand-name">Brenvik Optics</span>
    </div>

    <p class="device-type">Hydrophobic Intraocular Lens</p>

    <div class="lens-illustration" role="img" aria-label="Silver intraocular lens with two curved haptics"></div>

    <div class="product-block">
      <h1 class="product-name">Velonra</h1>
      <p class="product-feature">Aspheric with 360° Lens</p>
    </div>
  </main>
</body>
</html>
```